Elite Company Card

create a new dark colored, with metallic accents business card that people will not want to throw away

prefer rounded corners

Font styles to use
Serif

Requirements
Must have
• metallic accents
Nice to have
• 2 sided, the company logo prominent on one side the person and company info on the other side
Should not have
• no white

```html
<!DOCTYPE html>
<html lang="en">
<head>
<meta charset="utf-8">
<title>Crestline Autobody &amp; Paint Works – Business Card</title>
<link rel="stylesheet" href="https://fonts.googleapis.com/css2?family=Crimson+Text:wght@400;600;700&display=swap">
<style>
  :root {
    --backdrop: #2a2a2a;
    --brand-blue: #1d5ea3;
    --brand-blue-deep: #154a85;
    --brand-blue-light: #2a6fb6;
    --card-dark: #0f2238;
    --card-dark-edge: #0a1828;
    --metal-silver: #c9ccd1;
    --metal-bright: #e4e6ea;
    --metal-shadow: #8d9299;
    --ink-soft: #a9b4c2;
  }
  * { margin: 0; padding: 0; box-sizing: border-box; }
  html, body {
    width: 1200px; height: 660px; overflow: hidden;
    background: var(--backdrop);
    font-family: "Crimson Text", Georgia, serif;
  }
  .canvas {
    position: relative; width: 1200px; height: 660px;
    display: flex; align-items: center; justify-content: center; gap: 50px;
  }
  .card {
    position: relative; width: 520px; height: 300px;
    border-radius: 16px; overflow: hidden;
    box-shadow: 0 14px 30px rgba(0,0,0,.55);
  }

  /* Front side */
  .card-front {
    background: linear-gradient(135deg, var(--brand-blue-light), var(--brand-blue) 50%, var(--brand-blue-deep));
    display: flex; align-items: center; justify-content: center;
  }
  .front-wordmark {
    display: flex; align-items: center; gap: 18px;
    color: var(--metal-silver);
  }
  .front-wordmark .mark-dot {
    width: 46px; height: 46px; border-radius: 50%;
    background: var(--metal-silver);
  }
  .front-wordmark .name {
    font-weight: 700; font-size: 44px; line-height: 1.02;
    letter-spacing: 1px; text-transform: uppercase;
  }

  /* Back side */
  .card-back {
    background: linear-gradient(135deg, var(--card-dark), var(--card-dark-edge));
    color: var(--metal-bright);
  }
  .back-wordmark {
    position: absolute; left: 34px; top: 50px;
    font-weight: 700; font-size: 22px; line-height: 1.05;
    text-transform: uppercase; color: var(--metal-silver);
  }
  .holder {
    position: absolute; right: 34px; top: 24px; text-align: right;
  }
  .holder .person { font-size: 22px; font-weight: 600; line-height: 1.1; color: var(--metal-bright); }
  .holder .role { font-size: 13px; color: var(--ink-soft); }
  .location {
    position: absolute; font-size: 14px; line-height: 1.35;
    font-style: normal; color: var(--metal-bright);
  }
  .location h3 {
    font-size: 14px; font-weight: 700; text-transform: uppercase;
    letter-spacing: .5px; color: var(--metal-silver);
  }
  .location strong { font-weight: 700; color: var(--metal-silver); }
  .location-left { left: 34px; top: 140px; }
  .location-right { right: 34px; top: 112px; text-align: left; }
  .metal-rule {
    position: absolute; left: 0; right: 0; bottom: 46px; height: 4px;
    background: linear-gradient(90deg, var(--metal-shadow), var(--metal-bright), var(--metal-shadow));
  }
  .footer-band {
    position: absolute; left: 0; right: 0; bottom: 0; height: 40px;
    background: var(--brand-blue);
    display: flex; align-items: center; justify-content: flex-end;
    padding-right: 40px;
  }
  .footer-band .web {
    color: var(--metal-silver); font-size: 13px; letter-spacing: 6px;
  }
</style>
</head>
<body>
<main class="canvas">
  <section class="card card-front" aria-label="Card front">
    <div class="front-wordmark">
      <span class="mark-dot" aria-hidden="true"></span>
      <p class="name">Crestline<br>Autobody &amp;<br>Paint Works</p>
    </div>
  </section>

  <section class="card card-back" aria-label="Card back">
    <p class="back-wordmark">Crestline<br>Autobody &amp;<br>Paint Works</p>

    <div class="holder">
      <p class="person">John Doe</p>
      <p class="role">Owner</p>
    </div>

    <address class="location location-right">
      <h3>Harlow Location</h3>
      <p>2715 Fenwick Drive</p>
      <p>Millbrook, IL 62893</p>
      <p><strong>Phone:</strong> (555) 018-6470</p>
    </address>

    <address class="location location-left">
      <h3>Fenwick Location</h3>
      <p>1420 North Harlow Parkway</p>
      <p>Millbrook, IL 62890</p>
      <p><strong>Phone:</strong> (555) 014-2210</p>
    </address>

    <div class="metal-rule" aria-hidden="true"></div>
    <div class="footer-band"><span class="web">www.crestlineab.com</span></div>
  </section>
</main>
</body>
</html>
```